Tri-fold Brochure Design for New Custom Home Model

We need an expert to design a tri-fold brochure to showcase our new custom home model.<br/>The concept is as follow:<br/>We are introducing a fixed prize affordable custom home. We are trying to target landowners or homeowners who would like to build a custom home. We have a fixed design for exterior, interior. 3 level layout. Basement, main level, first floor.<br/>We have hand-drew the desired layout as you can see in the document attached names "hand-drawing". We would like the design to follow that idea.<br/>The required photos and info are attached. Please check out the attached documents here.<br/> The text content, material details can be found in the PDF file attached.

Target Market(s)

Home Owner, Land-owner, people who wants to build a new home

Industry/Entity Type

Residential Construction

Font styles to use
Sans Serif

Colors
ec1f27
fffefd

Requirements
Must have
• Formal text language, attractive design
Nice to have
• Most attractive and lead generating design
Should not have
• more than two colours, flashy design.

```html
<!DOCTYPE html>
<html lang="en">
<head>
<meta charset="utf-8">
<title>Harlow Homes Tri-fold Brochure</title>
<link href="https://fonts.googleapis.com/css2?family=Montserrat:wght@400;500;700;800&family=Oswald:wght@600&display=swap" rel="stylesheet">
<style>
:root{
  --accent:#ec1f27;
  --paper:#fffefd;
  --ink:#333333;
  --muted:#555555;
  --panel-grey:#f3f3f2;
  --box-grey:#e8e8e7;
  --on-accent:#fde3e4;
  --stage:#3d3d3d;
}
*{box-sizing:border-box;margin:0;padding:0}
html,body{width:865px;height:1200px;overflow:hidden;background:var(--stage)}
body{font-family:'Montserrat',sans-serif;color:var(--ink)}
.brochure{position:absolute;left:20px;top:308px;width:825px;height:584px;display:flex;box-shadow:0 10px 30px rgba(0,0,0,.5)}
.panel{position:relative;width:275px;height:584px;overflow:hidden}
.panel-about{background:var(--paper)}
.panel-why{background:var(--panel-grey);border-right:1px solid #ddd}
.panel-cover{background:var(--panel-grey)}
.heading{position:absolute;font-size:19px;font-weight:400;letter-spacing:.3px;color:var(--ink)}
.heading strong{color:var(--accent);font-weight:700}
.heading::after{content:"";position:absolute;left:0;top:30px;width:15px;height:2px;background:var(--accent)}
.about-heading{left:31px;top:30px}
.about-copy{position:absolute;left:31px;top:81px;width:240px;font-size:9.6px;line-height:13.6px;color:var(--muted);white-space:nowrap}
.kitchen-photo{position:absolute;left:0;top:227px;width:275px;height:249px;background:linear-gradient(160deg,#d9dbdc 0%,#c9c4b8 40%,#8d7a5c 75%,#6b5a45 100%)}
.partners{position:absolute;left:31px;top:506px;display:flex;align-items:center;gap:14px}
.partner-name{font-size:13px;font-weight:700;color:var(--ink)}
.badge{width:60px;height:22px;background:var(--accent);border-radius:3px}
.follow{position:absolute;left:59px;top:550px;display:flex;align-items:center;gap:5px;font-size:11px;font-weight:500;color:var(--ink)}
.follow .dot{width:15px;height:15px;border-radius:50%;background:var(--accent)}
.why-heading{left:35px;top:30px}
.reasons{position:absolute;left:36px;top:78px;display:grid;grid-template-columns:97px 97px;grid-auto-rows:89px;gap:8px 10px}
.reason{position:relative;background:var(--box-grey);padding:11px 5px 0;font-size:6.4px;line-height:9.4px;text-align:center;color:var(--muted)}
.reason b{color:var(--ink);font-weight:700}
.reason .num{position:absolute;left:2px;top:-4px;font-size:15px;font-weight:800;color:var(--accent)}
.contact{position:absolute;left:0;top:375px;width:275px;height:209px;background:var(--accent);color:var(--on-accent);text-align:center}
.contact-title{margin-top:25px;font-size:18px;font-weight:400;color:var(--paper)}
.contact-title strong{font-weight:700}
.contact-rule{width:15px;height:2px;background:var(--paper);margin:8px auto 10px}
.contact-line{font-size:11px;line-height:16px}
.contact-line svg{vertical-align:-1px;margin-right:3px}
.contact .gap{margin-top:7px}
.contact .web strong{font-weight:700;color:var(--paper)}
.brand{position:absolute;left:0;top:38px;width:275px;text-align:center;font-size:25px;font-weight:800;color:var(--ink);letter-spacing:.5px}
.brand-bar{position:absolute;left:130px;top:101px;width:145px;height:4px;background:var(--accent)}
.home-photo{position:absolute;left:0;top:105px;width:275px;height:270px;background:linear-gradient(180deg,#bcd3ea 0%,#d8e3ec 30%,#6d7d8c 55%,#4b5a46 85%,#3f5a2c 100%)}
.offer{position:absolute;left:0;top:375px;width:275px;height:209px;background:var(--accent)}
.price-tag{position:absolute;left:94px;top:348px;width:162px;height:64px}
.price{position:absolute;left:94px;top:354px;width:150px;text-align:center;font-size:20px;font-weight:800;color:var(--accent)}
.price-sub{position:absolute;left:94px;top:380px;width:150px;text-align:center;font-family:'Oswald',sans-serif;font-size:12.5px;font-weight:600;color:#111}
.earn{position:absolute;left:36px;top:420px;color:var(--paper);line-height:1}
.earn .row{display:flex;align-items:flex-end;gap:5px}
.earn .stack{display:flex;flex-direction:column}
.earn .also{font-size:19px;font-weight:400}
.earn .word{font-size:19px;font-weight:800}
.earn .amount{font-size:30px;font-weight:800;line-height:.9}
.earn .ask{margin-top:8px;font-size:17px;font-weight:800;letter-spacing:.3px}
.phone-pill{position:absolute;left:28px;top:516px;width:221px;height:36px;border:1.5px solid var(--paper);border-radius:18px;display:flex;align-items:center;color:var(--paper);font-size:22px;font-weight:800}
.phone-pill .icon{width:38px;height:38px;border-radius:50%;background:var(--paper);margin-left:-2px;margin-right:7px;display:flex;align-items:center;justify-content:center}
.offer-web{position:absolute;left:0;top:560px;width:275px;text-align:center;color:var(--on-accent);font-size:11.5px;letter-spacing:3px}
.offer-web strong{font-weight:700}
</style>
</head>
<body>
<main class="brochure">
  <section class="panel panel-about">
    <h2 class="heading about-heading">ABOUT <strong>US</strong></h2>
    <p class="about-copy">Lorem ipsum dolor sit amet, consectetur<br>adipiscing elit, sed do eiusmod tempor<br>incididunt ut labore et dolore magna aliqua.<br>Ut enim ad minim veniam, quis nostrud<br>exercitation ullamco laboris nisi ut aliquip<br>ex ea commodo consequat.<br>Duis aute irure dolor in reprehenderit in<br>voluptate velit esse cillum dolore eu fugiat<br>nulla pariatur.</p>
    <div class="kitchen-photo" role="img" aria-label="Photo of a modern kitchen with island and stools"></div>
    <div class="partners">
      <span class="partner-name">KBGUILD</span>
      <span class="partner-name">dwellio</span>
      <span class="badge" role="img" aria-label="Accreditation badge"></span>
    </div>
    <div class="follow">Follow Us -
      <span class="dot"></span><span class="dot"></span><span class="dot"></span><span class="dot"></span>
    </div>
  </section>

  <section class="panel panel-why">
    <h2 class="heading why-heading">WHY <strong>US</strong></h2>
    <div class="reasons">
      <div class="reason"><span class="num">1</span><b>Basement</b><br>A finished lower level with a recreation room, bedroom, full bath and laundry, ready to use from the first day.</div>
      <div class="reason"><span class="num">2</span><b>Main Level</b><br>An open kitchen with island, dining and living areas, a powder room and a covered front porch.</div>
      <div class="reason"><span class="num">3</span><b>First Floor</b><br>A primary suite with ensuite and walk-in closet, two further bedrooms and a shared full bath.</div>
      <div class="reason"><span class="num">4</span>Lorem ipsum dolor sit amet, consectetur adipiscing elit, sed do eiusmod tempor incididunt ut labore et dolore magna aliqua. Ut enim ad minim veniam, quis nostrud</div>
      <div class="reason"><span class="num">5</span>Lorem ipsum dolor sit amet, consectetur adipiscing elit, sed do eiusmod tempor incididunt ut labore et dolore magna aliqua. Ut enim ad minim veniam, quis nostrud</div>
      <div class="reason"><span class="num">6</span>Lorem ipsum dolor sit amet, consectetur adipiscing elit, sed do eiusmod tempor incididunt ut labore et dolore magna aliqua. Ut enim ad minim veniam, quis nostrud</div>
    </div>
    <div class="contact">
      <h3 class="contact-title">CONTACT <strong>INFO</strong></h3>
      <div class="contact-rule"></div>
      <svg width="10" height="13" viewBox="0 0 10 13" aria-hidden="true"><circle cx="5" cy="4" r="3" fill="none" stroke="#fffefd" stroke-width="1.3"/><path d="M5 7v5M2 12h6" stroke="#fffefd" stroke-width="1.3"/></svg>
      <p class="contact-line">Address line 1, Address line 1<br>Address line 2</p>
      <p class="contact-line gap"><svg width="10" height="8" viewBox="0 0 10 8" aria-hidden="true"><rect x=".5" y=".5" width="9" height="7" fill="none" stroke="#fde3e4"/><path d="M.5 .5l4.5 4 4.5-4" fill="none" stroke="#fde3e4"/></svg>info@harlowhomes.com</p>
      <p class="contact-line gap"><svg width="10" height="10" viewBox="0 0 10 10" aria-hidden="true"><circle cx="5" cy="5" r="4.3" fill="none" stroke="#fde3e4"/><path d="M3.3 3c.3 2 1.5 3.3 3.4 3.8" stroke="#fde3e4" fill="none"/></svg>0100 555 0199</p>
      <p class="contact-line gap web"><svg width="10" height="10" viewBox="0 0 10 10" aria-hidden="true"><circle cx="5" cy="5" r="4.3" fill="none" stroke="#fde3e4"/><ellipse cx="5" cy="5" rx="2" ry="4.3" fill="none" stroke="#fde3e4"/><path d="M.7 5h8.6" stroke="#fde3e4"/></svg>www.<strong>harlowhomes</strong>.com</p>
    </div>
  </section>

  <section class="panel panel-cover">
    <h1 class="brand">HARLOW HOMES</h1>
    <div class="brand-bar"></div>
    <div class="home-photo" role="img" aria-label="Photo of a three-level custom home with grey siding and a front porch"></div>
    <div class="offer"></div>
    <svg class="price-tag" viewBox="0 0 162 64" aria-hidden="true"><polygon points="10,0 150,0 162,64 0,64" fill="#fffefd"/></svg>
    <p class="price">$549,000</p>
    <p class="price-sub">This Could Your Home</p>
    <div class="earn">
      <div class="row">
        <div class="stack"><span class="also">ALSO,</span><span class="word">EARN</span></div>
        <span class="amount">$500/M</span>
      </div>
      <div class="ask">CALL US &amp; ASK HOW</div>
    </div>
    <div class="phone-pill">
      <span class="icon"><svg width="20" height="20" viewBox="0 0 24 24" aria-hidden="true"><path d="M6.6 10.8c1.4 2.8 3.8 5.1 6.6 6.6l2.2-2.2c.3-.3.7-.4 1-.2 1.1.4 2.3.6 3.6.6.6 0 1 .4 1 1V20c0 .6-.4 1-1 1C10.6 21 3 13.4 3 4c0-.6.4-1 1-1h3.5c.6 0 1 .4 1 1 0 1.3.2 2.5.6 3.6.1.3 0 .7-.2 1z" fill="#ec1f27"/></svg></span>
      0100 555 0199
    </div>
    <p class="offer-web">www.<strong>harlowhomes</strong>.com</p>
  </section>
</main>
</body>
</html>
```